New Tidewell 4 Group waste management business seeking web site

New project for business offering sustainable options within the waste industry.
Business called Tidewell 4 Group
Targeting the consumer & industry professionals the web site needs to be able to accommodate both.
Needs to have a modern clean feel.
Logo being designed by another pro and will be completed early next week and will be submitted soon after to be incorporated into the web page
Links to another web page i like very much to take into consideration.

Target Market(s)

Industry professionals, consumers and producers of all waste, Food, constructruction, commercial, retail .. etc..

Industry/Entity Type

Waste Management

Coding

Coded - Design and coding required

Number of Pages Required

5+ page

Font styles to use
Serif
Script

Requirements
Must have
• Flexabilty, all pages as in examples
Nice to have
• Open to offers you guys and gals are the pro's

```html
<!DOCTYPE html>
<html lang="en">
<head>
<meta charset="utf-8">
<title>Tidewell 4 Group</title>
<link rel="stylesheet" href="https://fonts.googleapis.com/css2?family=Nunito+Sans:wght@400;600;700;800&family=Libre+Baskerville:wght@400;700&family=EB+Garamond:ital,wght@0,400;1,400&display=swap">
<style>
:root{
  --ink:#222222;
  --nav:#333333;
  --hero:#aec8d3;
  --olive:#b5bb52;
  --olive-soft:#c9cc7a;
  --lilac:#a094b0;
  --sky:#aec8d3;
  --sage:#b5b87a;
  --rose:#dc8f8f;
  --pale:#f5f5f5;
  --muted:#a9a9a9;
  --white:#ffffff;
  --go:#1e6b0b;
  --go-text:#3fae1f;
}
*{margin:0;padding:0;box-sizing:border-box}
html,body{width:668px;height:1200px;overflow:hidden;background:var(--white)}
body{font-family:"Nunito Sans",Arial,sans-serif;color:var(--ink)}
.page{position:relative;width:668px;height:1200px;overflow:hidden}
.abs{position:absolute}

/* top navigation */
.topnav{left:0;top:0;width:668px;height:27px;background:var(--nav)}
.topnav a{position:absolute;top:0;height:27px;line-height:27px;color:var(--white);font-size:7.5px;text-decoration:none;text-align:center;border-left:1px solid #666}
.topnav .brand{color:var(--olive);font-weight:800;font-size:11px;border-left:1px solid #666}
.topnav .edge{border-right:1px solid #666}

/* hero */
.hero{left:0;top:27px;width:668px;height:186px;background:var(--hero)}
.social{left:55px;top:42px;display:flex;gap:3px}
.social span{width:10px;height:10px;background:#3a3a3a;border-radius:1px}
.search{left:503px;top:55px;width:110px;height:14px;border:1px solid #3c4a40;font-size:6px;padding-left:7px;line-height:12px;color:#222}
.kicker{left:263px;top:63px;width:140px;height:18px;border-top:1px solid #333;border-bottom:1px solid #333;font-family:"Libre Baskerville",Georgia,serif;font-size:6.5px;letter-spacing:2.2px;text-align:center;line-height:16px}
.hero-title{left:0;top:103px;width:668px;text-align:center;font-family:"Libre Baskerville",Georgia,serif;font-weight:700;font-size:19px;color:#2b2b2b}
.tagline{left:254px;top:150px;width:160px;text-align:center;color:var(--white);font-family:"Libre Baskerville",Georgia,serif;font-size:6.5px;letter-spacing:2.4px;line-height:8px}
.cta{left:265px;top:194px;width:139px;height:19px;background:var(--olive);color:var(--white);font-family:"EB Garamond",Georgia,serif;font-style:italic;font-size:10px;letter-spacing:.6px;text-align:center;line-height:19px}

/* section headings */
.heading{font-weight:800;font-size:9.5px;letter-spacing:2.8px}
.rule{height:0;border-top:1px dashed var(--olive-soft)}

/* services */
.service-art{width:101px;height:78px}
.service-name{width:130px;text-align:center;font-weight:800;font-size:7.5px;letter-spacing:.6px}
.service-note{width:105px;text-align:center;font-family:"EB Garamond",Georgia,serif;font-style:italic;font-size:8.5px;line-height:10px;color:var(--muted)}

/* work process */
.process{left:0;top:464px;width:668px;height:260px;background:var(--pale)}
.lead-italic{font-family:"EB Garamond",Georgia,serif;font-style:italic;font-size:9.5px;letter-spacing:.6px;color:#8a7f9d}
.body-copy{font-size:7px;line-height:9.2px;width:220px;color:#222}
.body-copy b{color:var(--olive);font-weight:700}

/* blog */
.post-art{width:76px;height:58px}
.post-title{width:78px;font-weight:800;font-size:7.4px;line-height:10px;text-transform:uppercase}
.post-date{font-size:4.8px;color:var(--muted)}

/* subscribe */
.subscribe{left:0;top:976px;width:668px;height:180px;background:var(--pale)}
.sub-copy{font-family:"EB Garamond",Georgia,serif;font-style:italic;font-size:10px;line-height:16.5px;width:140px;color:#222}
.field{width:139px;height:20px;background:var(--white);font-size:7px;color:#c3c3c3;padding-left:6px;line-height:20px}
.signup{left:396px;top:1094px;width:64px;height:21px;background:var(--go);color:var(--go-text);font-size:7px;text-align:center;line-height:21px;border-radius:2px}

/* footer */
.footer{left:0;top:1156px;width:668px;height:44px;background:var(--nav)}
.foot-brand{left:55px;top:1167px;color:#e5e5e5;font-weight:800;font-size:7.5px}
.foot-links{color:#e5e5e5;font-size:5.5px;line-height:6.5px}
.legal{left:131px;top:1190px;font-size:5.5px;color:var(--olive)}
.legal span{color:#999;margin:0 5px}
.copyright{right:55px;top:1190px;font-size:5.5px;color:var(--olive)}
</style>
</head>
<body>
<div class="page">

  <nav class="abs topnav">
    <a href="#" style="left:186px;width:38px">Work</a>
    <a href="#" style="left:224px;width:40px">Insight</a>
    <a href="#" class="brand" style="left:264px;width:140px">Tidewell 4 Group</a>
    <a href="#" style="left:404px;width:44px">Services</a>
    <a href="#" style="left:448px;width:40px">About</a>
    <a href="#" class="edge" style="left:488px;width:52px">Contact Us</a>
  </nav>

  <header class="abs hero"></header>
  <div class="abs social" aria-label="Social links"><span></span><span></span><span></span><span></span></div>
  <div class="abs search">Search</div>
  <div class="abs kicker">ECO-FRIENDLY RECYCLING</div>
  <h1 class="abs hero-title">Tidewell 4 Group</h1>
  <p class="abs tagline">UNLOCKING THE POWER IN RECYCLABILITY</p>
  <div class="abs cta">Learn More &gt;</div>

  <!-- services -->
  <h2 class="abs heading" style="left:0;width:668px;text-align:center;top:241px">OUR SERVICES</h2>
  <div class="abs rule" style="left:288px;top:258px;width:92px"></div>

  <div class="abs service-art" role="img" aria-label="Leaf emblem on a light blue botanical pattern" style="left:114px;top:297px;background:radial-gradient(circle at 50% 50%,var(--sky) 0 30px,#dde9ee 31px)"></div>
  <div class="abs service-art" role="img" aria-label="Leaf emblem on a light green botanical pattern" style="left:226px;top:297px;background:radial-gradient(circle at 50% 50%,var(--sage) 0 30px,#e3e5c2 31px)"></div>
  <div class="abs service-art" role="img" aria-label="Leaf emblem on a light lilac botanical pattern" style="left:340px;top:297px;background:radial-gradient(circle at 50% 50%,var(--lilac) 0 30px,#ddd8e4 31px)"></div>
  <div class="abs service-art" role="img" aria-label="Leaf emblem on a light pink botanical pattern" style="left:454px;top:297px;background:radial-gradient(circle at 50% 50%,var(--rose) 0 30px,#f0cece 31px)"></div>

  <div class="abs service-name" style="left:99px;top:390px">COMMERCIAL WASTE</div>
  <div class="abs service-name" style="left:212px;top:390px">DOMESTIC WASTE</div>
  <div class="abs service-name" style="left:325px;top:390px">RECYCLING</div>
  <div class="abs service-name" style="left:440px;top:390px">PACKAGING COMPLIANCE</div>

  <p class="abs service-note" style="left:112px;top:409px">Solutions for business</p>
  <p class="abs service-note" style="left:225px;top:409px">Having a clear out or doing up a property ? We can help</p>
  <p class="abs service-note" style="left:338px;top:409px">Our promise to you of 0% to landfill</p>
  <p class="abs service-note" style="left:452px;top:409px">Solutions for business</p>

  <!-- work process -->
  <section class="abs process"></section>
  <h2 class="abs heading" style="left:55px;top:507px">OUR WORK PROCESS</h2>
  <div class="abs rule" style="left:55px;top:528px;width:132px"></div>
  <p class="abs lead-italic" style="left:55px;top:557px">Let us show our work process</p>
  <p class="abs body-copy" style="left:55px;top:582px">Lorem ipsum dolor sit amet, consectetur adipiscing elit, sed do eiusmod tempor incididunt ut labore et dolore magna aliqua. Ut enim ad minim veniam, quis nostrud exercitation ullamco laboris nisi ut aliquip ex ea commodo <b>consequat.</b></p>

  <svg class="abs" style="left:280px;top:560px" width="340" height="110" viewBox="0 0 340 110">
    <circle cx="54" cy="54" r="51" fill="var(--lilac)" stroke="#333" stroke-width=".8"/>
    <circle cx="168" cy="54" r="51" fill="var(--sky)" stroke="#333" stroke-width=".8"/>
    <circle cx="282" cy="54" r="51" fill="var(--sage)" stroke="#333" stroke-width=".8"/>
    <g font-family="EB Garamond, Georgia, serif" font-style="italic" font-size="9" fill="#ffffff" text-anchor="middle" letter-spacing=".6">
      <text x="54" y="63">Discover</text>
      <text x="168" y="63">Design</text>
      <text x="282" y="63">Deliver</text>
    </g>
  </svg>

  <!-- blog -->
  <h2 class="abs heading" style="left:55px;top:753px">FROM THE BLOG</h2>
  <div class="abs rule" style="left:55px;top:774px;width:105px"></div>

  <div class="abs post-art" role="img" aria-label="Blue refuse sacks piled at a depot" style="left:55px;top:803px;background:linear-gradient(160deg,#2d5c9e,#16346a 60%,#5d6f88)"></div>
  <div class="abs post-art" role="img" aria-label="Food scraps and vegetable peelings" style="left:143px;top:803px;background:linear-gradient(135deg,#8a6a30,#c96a2a 45%,#5f7f34)"></div>
  <div class="abs post-art" role="img" aria-label="Crushed drink cans for recycling" style="left:234px;top:803px;background:linear-gradient(135deg,#c7362b,#d9b43b 45%,#2e6f3e)"></div>
  <div class="abs post-art" role="img" aria-label="Baled cardboard under a blue sky" style="left:321px;top:803px;background:linear-gradient(180deg,#4f7fc4 0 30%,#b8a07e 30%,#8a735a)"></div>
  <div class="abs post-art" role="img" aria-label="Food scraps and vegetable peelings" style="left:409px;top:803px;background:linear-gradient(135deg,#8a6a30,#c96a2a 45%,#5f7f34)"></div>
  <div class="abs post-art" role="img" aria-label="Crushed drink cans for recycling" style="left:499px;top:803px;background:linear-gradient(135deg,#c7362b,#d9b43b 45%,#2e6f3e)"></div>

  <div class="abs post-title" style="left:55px;top:875px">Solutions for business</div>
  <div class="abs post-date" style="left:55px;top:900px">5th Dec 15</div>
  <div class="abs post-title" style="left:143px;top:875px">Having a clear out or doing up a property ? We can help</div>
  <div class="abs post-date" style="left:143px;top:921px">5th Dec 15</div>
  <div class="abs post-title" style="left:234px;top:875px">Our promise to you of 0% to landfill</div>
  <div class="abs post-date" style="left:234px;top:910px">5th Dec 15</div>
  <div class="abs post-title" style="left:321px;top:875px">Solutions for business</div>
  <div class="abs post-date" style="left:321px;top:900px">5th Dec 15</div>
  <div class="abs post-title" style="left:409px;top:875px">Having a clear out or doing up a property ? We can help</div>
  <div class="abs post-date" style="left:409px;top:921px">5th Dec 15</div>
  <div class="abs post-title" style="left:499px;top:875px">Our promise to you of 0% to landfill</div>
  <div class="abs post-date" style="left:499px;top:910px">5th Dec 15</div>

  <!-- subscribe -->
  <section class="abs subscribe"></section>
  <div class="abs" role="img" aria-label="Climbing vine with leaves and berries" style="left:94px;top:974px;width:26px;height:180px;background:linear-gradient(180deg,rgba(160,148,176,.15),rgba(160,148,176,.45) 50%,rgba(160,148,176,.15))"></div>
  <h2 class="abs heading" style="left:169px;top:1004px">SUBSCRIBE</h2>
  <div class="abs rule" style="left:169px;top:1025px;width:104px"></div>
  <p class="abs sub-copy" style="left:169px;top:1036px">Gain insight to our exclusive Mega Trends feature &amp; sign up to our quarterly reports</p>
  <div class="abs field" style="left:320px;top:1003px">Name</div>
  <div class="abs field" style="left:320px;top:1034px">Email</div>
  <div class="abs field" style="left:320px;top:1064px">Website</div>
  <div class="abs signup">Sign Up</div>

  <!-- footer -->
  <footer class="abs footer"></footer>
  <div class="abs foot-brand">Tidewell4Group</div>
  <div class="abs foot-links" style="left:131px;top:1166px">Work<br>Insight<br>Services</div>
  <div class="abs foot-links" style="left:163px;top:1166px">About<br>Contact Us</div>
  <div class="abs legal">Privacy Policy<span>|</span>Terms of Use<span>|</span>Accessibility</div>
  <div class="abs copyright">© 2015 Tidewell4Group</div>

</div>
</body>
</html>
```